hillcrest coolant & muffler (the gear for every motoring job)

we need a business card design for a company that started out as a radiator shop cleaning repairing recoring or selling new radiators. then we got into fuel tank repair cleaning repairing and lining if the tank leaks we fix it if it has jelled gas or rust we clean it then roll a liner in it no more fuel touching the tank.later we started doing exhaust from small single exhaust to custom duels.now the first of the year we started selling and repairing tires. Now we are doing alignments . we also do brakes and suspension and oil changes we need some way to get the message out about all we do.I would like to see some flare in the writing of the name of the business but still easily read.read. I'm thinking on black and red as colors.but im open for suggestions Id like it to be eye catching and memorable.
Updates

Project Deadline Extended
Reason: i dont have a logo for you please make me one

Target Market(s)

4 wheel alignment-tires new and used.radiator clean and repair recores new complete radiators.fuel tank cleaning and repair and liners.exhaust standard single and custom duels.cars,trucks, and buses.from the youngest driver to the oldest.

Industry/Entity Type

Automotive

Contact Information for Business Card

Hillcrest Coolant & Muffler Inc. 418 S Pembrook lane Marlow in.46902 574-208-6143 m-f 9-5 sat 9-12 for tires call 812-365-9497m-f8-5 sat8-12

Font styles to use
Decorative

Colors
000000
ec1f27

Requirements
Must have
• eye catching colors and letters. both phone numbers and hours.logo
Nice to have
• list of things we can do

```html
<!DOCTYPE html>
<html lang="en">
<head>
<meta charset="utf-8">
<title>Hillcrest Coolant &amp; Muffler – Business Card</title>
<link href="https://fonts.googleapis.com/css2?family=Saira:wght@400;500;600&display=swap" rel="stylesheet">
<style>
  :root {
    --ink: #1d1d1d;
    --black: #000000;
    --red: #ec1f27;
    --paper: #ffffff;
    --backdrop: #e9e7e3;
    --muted: #3a3a3a;
  }
  * { box-sizing: border-box; margin: 0; padding: 0; }
  html, body {
    width: 1200px; height: 892px; overflow: hidden;
    background: var(--backdrop);
    font-family: "Saira", sans-serif;
    color: var(--ink);
  }
  .sheet {
    position: relative; width: 1200px; height: 892px;
    display: flex; flex-direction: column; align-items: center; justify-content: center; gap: 60px;
  }
  .card {
    position: relative; width: 560px; height: 320px;
    background: var(--paper); overflow: hidden;
    box-shadow: 0 6px 18px rgba(0,0,0,.18);
  }
  .card__wave { position: absolute; left: 0; bottom: 0; width: 100%; height: 100%; }

  /* front */
  .front__brand { position: absolute; left: 60px; top: 62px; display: flex; align-items: center; gap: 22px; }
  .brand__mark { width: 58px; height: 58px; background: var(--red); flex: none; }
  .front__name { font-size: 74px; font-weight: 600; line-height: .9; letter-spacing: -1px; color: var(--ink); }
  .front__tagline { font-size: 40px; font-weight: 500; line-height: 1.2; color: var(--ink); margin-top: 6px; }

  /* back */
  .back__brand { position: absolute; left: 170px; top: 36px; display: flex; align-items: center; gap: 12px; }
  .back__brand .brand__mark { width: 26px; height: 26px; }
  .back__name { font-size: 38px; font-weight: 600; line-height: .9; color: var(--ink); }
  .back__tagline { font-size: 18px; font-weight: 500; color: var(--ink); }
  .back__contact { position: absolute; left: 170px; top: 150px; font-size: 15px; line-height: 1.75; color: var(--muted); }
  .contact__row { white-space: nowrap; }
  .contact__row span + span { margin-left: 12px; }
</style>
</head>
<body>
<main class="sheet">
  <section class="card card--front">
    <div class="front__brand">
      <div class="brand__mark"></div>
      <div>
        <div class="front__name">Hillcrest</div>
        <div class="front__tagline">Coolant &amp; Muffler</div>
      </div>
    </div>
    <svg class="card__wave" viewBox="0 0 560 320" preserveAspectRatio="none" aria-hidden="true">
      <path d="M0 252 C150 236 260 268 380 258 C460 251 520 240 560 236 L560 250 C500 256 440 268 380 272 C260 280 150 254 0 268 Z" fill="var(--black)"/>
      <path d="M0 278 C150 264 260 286 380 280 C460 276 520 262 560 256 L560 320 L0 320 Z" fill="var(--red)"/>
    </svg>
  </section>

  <section class="card card--back">
    <svg class="card__wave" viewBox="0 0 560 320" preserveAspectRatio="none" aria-hidden="true">
      <path d="M0 0 L46 0 C30 80 90 150 110 220 C122 262 124 296 118 320 L0 320 Z" fill="var(--red)"/>
      <path d="M56 0 C42 80 104 150 124 220 C136 262 138 296 132 320 L122 320 C128 294 126 262 114 222 C94 152 34 82 48 0 Z" fill="var(--black)"/>
    </svg>
    <div class="back__brand">
      <div class="brand__mark"></div>
      <div>
        <div class="back__name">Hillcrest</div>
        <div class="back__tagline">Coolant &amp; Muffler Inc</div>
      </div>
    </div>
    <div class="back__contact">
      <div class="contact__row">418 S Pembrook lane Marlow in.46902</div>
      <div class="contact__row"><span>574-208-6143</span><span>:</span><span>mon - fri 9 - 5&nbsp; sat 9 - 12</span><span>for tires call</span></div>
      <div class="contact__row"><span>574-208-7381</span><span>:</span><span>mon - fri 8 - 5&nbsp; sat 8 - 12</span><span>for tires call</span></div>
    </div>
  </section>
</main>
</body>
</html>
```